Business cards for Brightmarrow Consulting with the following info for the front side:

Brightmarrow Consulting
Executive Coaching and Human Capital Strategy
www.brightmarrow.example

Lorena Vaduvic
Principal
lorena@brightmarrow.example
+1 604 555 0172

Black background, text using the colours of the logo - enclosed.

The back side of the business card should feature the logo in the middle, with "Executive Coaching and Human Capital Strategy" on top and "www.brightmarrow.example" below.

```html
<!DOCTYPE html>
<html lang="en">
<head>
<meta charset="utf-8">
<title>Brightmarrow Consulting – Business Cards</title>
<link rel="stylesheet" href="https://fonts.googleapis.com/css2?family=Oswald:wght@500&family=Work+Sans:wght@400;500&display=swap">
<style>
  :root {
    --backdrop: #121212;
    --card: #1d1d1d;
    --card-edge: #262626;
    --silver: #c4c4c4;
    --silver-soft: #9e9e9e;
    --silver-dim: #7d7d7d;
  }
  * { box-sizing: border-box; margin: 0; padding: 0; }
  html, body {
    width: 1200px; height: 900px; overflow: hidden;
    background: radial-gradient(ellipse at 50% 30%, #2a2a2a 0%, var(--backdrop) 75%);
    font-family: "Work Sans", Arial, sans-serif;
  }
  .sheet {
    width: 1200px; height: 900px;
    display: flex; flex-direction: column; align-items: center; justify-content: center;
    gap: 44px;
  }
  .card {
    width: 660px; height: 377px;
    background: linear-gradient(160deg, #242424 0%, var(--card) 55%, #181818 100%);
    border: 1px solid var(--card-edge);
    box-shadow: 0 18px 40px rgba(0,0,0,.55);
    position: relative;
  }
  /* Logo side */
  .card--brand {
    display: flex; flex-direction: column; align-items: center; justify-content: center;
  }
  .brand {
    display: flex; align-items: center; gap: 16px;
    margin-top: -10px;
  }
  .brand__dot {
    width: 50px; height: 50px; border-radius: 50%;
    border: 2px solid var(--silver);
  }
  .brand__name {
    font-family: "Work Sans", Arial, sans-serif;
    font-weight: 500; font-size: 40px; letter-spacing: 1px;
    color: var(--silver); text-transform: uppercase;
  }
  .brand__tagline {
    margin-top: 46px;
    font-size: 15px; letter-spacing: .6px; color: var(--silver-soft);
  }
  .brand__web {
    margin-top: 4px;
    font-size: 15px; letter-spacing: .6px; color: var(--silver-soft);
  }
  /* Contact side */
  .card--contact {
    display: flex; align-items: center; justify-content: center;
  }
  .person { text-align: right; padding-right: 26px; }
  .person__name {
    font-family: "Oswald", "Arial Narrow", sans-serif;
    font-weight: 500; font-size: 34px; letter-spacing: .5px;
    color: var(--silver-dim); text-transform: uppercase; line-height: 1.1;
  }
  .person__role { font-size: 16px; color: var(--silver-dim); margin-top: 2px; letter-spacing: .5px; }
  .divider { width: 2px; height: 66px; background: var(--silver-dim); margin-top: 24px; }
  .contacts { list-style: none; padding-left: 26px; margin-top: 30px; }
  .contacts li {
    display: flex; align-items: center; gap: 10px;
    font-size: 17px; letter-spacing: .6px; color: var(--silver); line-height: 1.45;
  }
  .contacts svg { width: 12px; height: 12px; flex: none; }
</style>
</head>
<body>
<main class="sheet">
  <section class="card card--brand">
    <div class="brand">
      <span class="brand__dot"></span>
      <span class="brand__name">Brightmarrow</span>
    </div>
    <p class="brand__tagline">Executive Coaching and Human Capital Strategy</p>
    <p class="brand__web">www.brightmarrow.example</p>
  </section>

  <section class="card card--contact">
    <div class="person">
      <h1 class="person__name">Lorena Vaduvic</h1>
      <p class="person__role">Principal</p>
    </div>
    <span class="divider"></span>
    <ul class="contacts">
      <li>
        <svg viewBox="0 0 12 12" aria-hidden="true"><path d="M2.5 1 L4.5 1 L5 3.5 L3.8 4.4 Q4.8 6.8 7.6 8.2 L8.5 7 L11 7.5 L11 9.5 Q10.5 11 9 11 Q2 10 1 3 Q1 1.5 2.5 1 Z" fill="var(--silver)"/></svg>
        +1 604 555 0172
      </li>
      <li>
        <svg viewBox="0 0 12 12" aria-hidden="true"><rect x="1" y="2.5" width="10" height="7" fill="none" stroke="var(--silver)" stroke-width="1.2"/><path d="M1 2.5 L6 6.5 L11 2.5" fill="none" stroke="var(--silver)" stroke-width="1.2"/></svg>
        lorena@brightmarrow.example
      </li>
      <li>
        <svg viewBox="0 0 12 12" aria-hidden="true"><circle cx="6" cy="6" r="5" fill="none" stroke="var(--silver)" stroke-width="1.1"/><ellipse cx="6" cy="6" rx="2.2" ry="5" fill="none" stroke="var(--silver)" stroke-width="1"/><path d="M1 6 H11" stroke="var(--silver)" stroke-width="1"/></svg>
        www.brightmarrow.example
      </li>
    </ul>
  </section>
</main>
</body>
</html>
```